business card deign

Logo needs the following on it.
1. attached logo
2. Tagline - "If it keeps a drink cold or the party going...we do it!"
3. Name- Delia Fenwick, Founder and CPO
4. Address - 418 E. Harlow Avenue, Ste 2204, Tampa, FL. 33719
5. Phone - 720.555.0187

```html
<!DOCTYPE html>
<html lang="en">
<head>
<meta charset="utf-8">
<title>Briska — Business Card</title>
<link rel="stylesheet" href="https://fonts.googleapis.com/css2?family=Montserrat:wght@400;700&display=swap">
<style>
  :root {
    --backdrop: #e9e6e1;
    --card-light: #ffffff;
    --card-dark: #000000;
    --ink: #111111;
    --ink-soft: #1e1e1e;
    --paper: #ffffff;
  }
  * { margin: 0; padding: 0; box-sizing: border-box; }
  html, body {
    width: 900px;
    height: 1200px;
    overflow: hidden;
    background: var(--backdrop);
    font-family: "Montserrat", Arial, sans-serif;
  }
  .canvas {
    position: relative;
    width: 900px;
    height: 1200px;
  }
  .card {
    position: absolute;
    box-shadow: 0 8px 22px rgba(0, 0, 0, 0.25);
  }
  .card--front {
    left: 80px; top: 130px;
    width: 742px; height: 442px;
    border-radius: 22px;
    background: var(--card-light);
    color: var(--ink);
  }
  .card--back {
    left: 78px; top: 638px;
    width: 744px; height: 440px;
    border-radius: 28px;
    background: var(--card-dark);
    color: var(--paper);
  }
  .holder-name {
    position: absolute;
    left: 35px; top: 68px;
    font-size: 25px;
    font-weight: 700;
    letter-spacing: 0.2px;
  }
  .holder-title {
    position: absolute;
    left: 35px; top: 100px;
    font-size: 15px;
    font-weight: 400;
    color: var(--ink-soft);
  }
  .address {
    position: absolute;
    left: 35px; top: 268px;
    font-size: 16px;
    line-height: 21px;
    font-style: normal;
    color: var(--ink-soft);
  }
  .contact-list {
    position: absolute;
    left: 37px; top: 318px;
    list-style: none;
    font-size: 15.5px;
    color: var(--ink-soft);
  }
  .contact-item {
    display: flex;
    align-items: center;
    height: 31px;
  }
  .contact-icon {
    width: 15px; height: 15px;
    margin-right: 11px;
    fill: var(--ink);
  }
  .brand {
    position: absolute;
    display: flex;
    align-items: center;
    justify-content: center;
    gap: 12px;
    width: 320px;
    font-size: 32px;
    font-weight: 700;
    line-height: 1;
  }
  .brand-dot {
    width: 20px; height: 20px;
    border-radius: 50%;
    background: currentColor;
  }
  .card--front .brand {
    left: 345px; top: 224px;
    color: var(--ink);
  }
  .card--back .brand {
    left: 212px; top: 180px;
    color: var(--paper);
  }
  .tagline {
    position: absolute;
    left: 0; right: 0; top: 382px;
    text-align: center;
    font-size: 16.5px;
    font-weight: 400;
  }
</style>
</head>
<body>
<main class="canvas">

  <section class="card card--front" aria-label="Card front">
    <h1 class="holder-name">Delia Fenwick</h1>
    <p class="holder-title">Founder and CPO</p>
    <address class="address">418 E. Harlow Avenue, Ste 2204,<br>Tampa, FL. 33719</address>
    <ul class="contact-list">
      <li class="contact-item">
        <svg class="contact-icon" viewBox="0 0 24 24" aria-hidden="true"><path d="M6.6 10.8a15.1 15.1 0 0 0 6.6 6.6l2.2-2.2a1 1 0 0 1 1-.25 11.4 11.4 0 0 0 3.6.57 1 1 0 0 1 1 1V20a1 1 0 0 1-1 1A17 17 0 0 1 3 4a1 1 0 0 1 1-1h3.5a1 1 0 0 1 1 1c0 1.25.2 2.45.57 3.57a1 1 0 0 1-.25 1z"/></svg>
        720.555.0187
      </li>
      <li class="contact-item">
        <svg class="contact-icon" viewBox="0 0 24 24" aria-hidden="true"><path d="M2 5h20v2l-10 6.5L2 7z"/><path d="M2 9l10 6.5L22 9v10H2z"/></svg>
        info@briska.com
      </li>
      <li class="contact-item">
        <svg class="contact-icon" viewBox="0 0 24 24" aria-hidden="true"><circle cx="12" cy="12" r="10" fill="none" stroke="#111" stroke-width="2.4"/><path d="M12 2a10 10 0 0 1 0 20 15 15 0 0 1 0-20z M2 12h20" fill="none" stroke="#111" stroke-width="2"/></svg>
        www.briska.com
      </li>
    </ul>
    <div class="brand"><span class="brand-dot" aria-hidden="true"></span>Briska</div>
  </section>

  <section class="card card--back" aria-label="Card back">
    <div class="brand"><span class="brand-dot" aria-hidden="true"></span>Briska</div>
    <p class="tagline">If it keeps a drink cold or the party going...we do it</p>
  </section>

</main>
</body>
</html>
```